Wordpress Design Project

WHO WE ARE:
Bright Path Web Growth is not just another SEO or PPC company. We work with our clients to help them grow their business and achieve their goals. Our commitment to doing what is best for the customer, is why we have grown so quickly. We believe our business is not about advertising BUT about connecting customers & growing our clients businesses. We see our product as helping people, not selling a product.

PROJECT OVERVIEW:
I need to create a wordpress website for my business, www.brightpathwebgrowth.com.au

I need a whole new site created showing all of my services. The services include:
NOTE: These are not the main focus of the home page.

Consulting & Strategy Planning
Search Engine Optimisation
Pay Per Click
Re-Marketing

Once I have selected the top home page design, I will need a product and blog page designed.

SITE DESIGN:
If I was to explain the kind of style I am looking for, it would be high-street, New York agency look, web 2.0. Clean, elegant, stylish, high quality and simple looking. Kind of like you would expect from an quince website.

Think of car advertising, the closest to the target market & look/feel Im looking for would be Ravenmotor, Korel, Tamar, Brandin, Zepra.

However, I am open to any design style.

DO NOT let this restrict your creativity BUT here are some websites I like the look of.

Home page:
http://www.layoutfoundry.example/demo/52816.html
https://www.vantorix.example/intl/en/halo/devices/
http://www.vantorix.example/intl/en/halo/devices/features-different.html
http://www.layoutfoundry.example/demo/47190.html
https://www.vantorix.example/intl/en/halo/browser/features.html

Product Page:
http://www.vantorix.example/intl/en/halo/devices/buynow.html#instore

NOTE: I just added a file called "I like this color scheme.png" you can play around with something like this as well.
Updates

Please do not use the content from my current website. That is for a PPC service, the new site is for an full service agency.

Also, the message/tagline is the feature or most prominent element of the website..... Not the services we offer, these are secondary.

Great designs so far everyone, but I think I'm looking a little simpler and less crowded.  Closer to the sample sites I sent.... keep em coming.

Also, I would prefer that the 4 services, do not visually over power the tag line.  The 4 services are not important to the home page.

Lets make this easy, since every design I receive is almost the same...

Make the design look something like these 2 websites.
https://www.vantorix.example/intl/en/halo/browser/features.html#simplicity

Target Market(s)

Business Owners and entreprenuers who are well established, typically in the 35-60 year old range and spend 100k-1m in advertising per year. They big brands that target these people are Ravenmotor, Korel, Tamar, Brandin, Zepra, this should give you the feel for what I am after.

Industry/Entity Type

Advertising

Requirements
Must have
• 1. Navigations: Home, Services, About Us, Blog, Contact Us

2. The main home page words should be.... "We Grow Your Business Online" and "Clear Aim, Clear Plan, Clear Team, Bright Path Web Growth" (should use logo for last one)
I would like to see this tagline somewhere in the site "We Don't Want to be the Biggest, Just the Best!"

3. Product page must have a contact form with (name, email, phone, website)
This form must show an offer of "Free Strategy Sessions, Double your website leads", I have included an image to show as an example for the lead form "lead form example.png", see attached.

Nice to have
• I would like to see 1 or 2 of these idea's in the design.

1. I have attached some logos for Bidlane & Metricove certifications + Web association logo you can use for design purposes.

2. You can put company logo's in the design and I can change them to my clients logos at a later date.

3. Testimonials

4. Since our business is about people, pictures of people like business owners, customers using technology such as an slate, or anything like that would be good. However, is not necessary. Some idea: http://www.peerlattice.example/advertising
Should not have
• There will be no video on the design.

```html
<!DOCTYPE html>
<html lang="en">
<head>
<meta charset="utf-8">
<title>Bright Path Web Growth</title>
<link rel="stylesheet" href="https://fonts.googleapis.com/css2?family=Cabin:wght@400;500;600&family=Cabin+Condensed:wght@500&family=Open+Sans:wght@400;700&display=swap">
<style>
  :root{
    --page:#6b6a75;
    --panel-top:#b2b2b7;
    --panel-mid:#c6c6ca;
    --panel-bottom:#84848e;
    --white:#ffffff;
    --logo-text:#d8d8dc;
    --brand-blue:#2f7fd0;
    --nav-blue:#4fa8d8;
    --lime:#b7cf2c;
    --accent-red:#e0553a;
    --map-red:#d95f48;
    --ink:#2a2a2e;
    --form-dark:#39393d;
    --field-a:#6e6e72;
    --field-b:#a9a9ad;
  }
  *{box-sizing:border-box;margin:0;padding:0}
  html,body{width:1200px;height:675px;overflow:hidden}
  body{background:var(--page);position:relative;font-family:"Cabin",sans-serif;color:var(--white)}

  .brand{position:absolute;left:232px;top:28px;display:flex;align-items:center;gap:14px}
  .brand-dot{width:46px;height:46px;border-radius:50%;background:var(--brand-blue)}
  .brand-name{font-family:"Cabin",sans-serif;font-weight:600;font-size:26px;color:var(--logo-text);letter-spacing:.2px}

  .main-nav{position:absolute;left:231px;top:97px;display:flex;align-items:center;font-family:"Cabin Condensed",sans-serif;font-size:17px}
  .main-nav a{color:var(--white);text-decoration:none}
  .main-nav a.is-current{color:var(--nav-blue)}
  .nav-sep{display:inline-block;width:2px;height:20px;background:var(--nav-blue);margin:0 16px 0 17px}

  .call-us{position:absolute;left:752px;top:97px;font-family:Arial,sans-serif;font-size:18px;color:var(--lime)}

  .content-panel{position:absolute;left:198px;top:130px;width:795px;height:506px;border-radius:6px;
    background:linear-gradient(180deg,var(--panel-top) 0%,var(--panel-mid) 40%,var(--panel-bottom) 100%)}

  .world-map{position:absolute;left:238px;top:160px;width:210px;height:125px;border-radius:40px 60px 30px 50px;
    background:radial-gradient(ellipse at 50% 45%,var(--map-red) 55%,rgba(217,95,72,0) 75%)}

  .services{position:absolute;left:569px;top:175px}
  .services h2{font-family:"Cabin",sans-serif;font-weight:500;font-size:16px;color:var(--accent-red);margin-bottom:20px}
  .services ul{list-style:none;font-family:"Open Sans",sans-serif;font-size:13px;line-height:14.6px}

  .headline{position:absolute;left:263px;top:299px;font-family:"Cabin",sans-serif;font-weight:500;font-size:16.5px;line-height:21.5px}
  .headline span{display:block}

  .photo{position:absolute;top:380px;width:124px;height:83px;border:2px solid var(--brand-blue)}
  .photo--team{left:260px;background:linear-gradient(160deg,#e8e8ea,#9a9aa2)}
  .photo--signing{left:415px;background:linear-gradient(160deg,#3a2a22,#d8c8b8 70%,#f0ece8)}
  .photo--devices{left:568px;background:linear-gradient(160deg,#d6d2c8,#4a4a4e 60%,#b8b4a8)}

  .testimonials-title{position:absolute;left:237px;top:495px;font-family:"Cabin",sans-serif;font-weight:500;font-size:14px;color:var(--ink)}
  .testimonial{position:absolute;top:521px;width:136px;padding-left:11px;color:var(--ink)}
  .testimonial::before{content:"\201C";position:absolute;left:0;top:-2px;color:var(--accent-red);font-size:12px;font-weight:700}
  .testimonial p{font-family:"Open Sans",sans-serif;font-weight:700;font-size:6.2px;line-height:8px}
  .testimonial .who{margin-top:10px;font-size:6px}
  .testimonial .site{font-size:6px;color:var(--accent-red)}
  .t1{left:250px}.t2{left:404px}.t3{left:559px}
  .see-all{position:absolute;left:260px;top:604px;font-family:"Open Sans",sans-serif;font-size:9px;color:var(--ink)}

  .offer{position:absolute;left:755px;top:255px;width:188px;height:91px;
    background:linear-gradient(180deg,rgba(140,140,148,0) 0%,#8c8c94 35%,#85858d 100%)}
  .offer-badge{position:absolute;left:11px;top:7px;width:47px;height:47px;border-radius:50%;background:var(--lime);
    font-family:"Cabin",sans-serif;font-weight:600;font-size:18px;line-height:47px;text-align:center;color:var(--white)}
  .offer-line{position:absolute;font-family:"Cabin",sans-serif;color:var(--lime);white-space:nowrap}
  .offer-line--sessions{left:65px;top:24px;font-size:13px}
  .offer-line--here{left:97px;top:41px;font-size:16px}
  .offer-line--leads{left:56px;top:61px;font-size:14px;color:var(--white)}
  .offer-line--leads span{color:var(--lime)}

  .lead-form{position:absolute;left:740px;top:345px;width:218px;height:243px;border-radius:10px;background:var(--form-dark)}
  .lead-form label{position:absolute;left:17px;font-family:"Open Sans",sans-serif;font-size:11.5px;color:var(--lime)}
  .lead-form .field{position:absolute;left:16px;width:188px;height:15px;border:0;
    background:linear-gradient(90deg,var(--field-a) 0%,var(--field-b) 50%,var(--field-a) 100%)}
  .lead-form button{position:absolute;left:16px;top:196px;width:97px;height:15px;border:0;
    background:linear-gradient(180deg,#d4e56a,#95ad1e);font-family:Arial,sans-serif;font-size:11px;color:var(--ink)}

  .site-footer{position:absolute;left:236px;top:645px;font-family:Arial,sans-serif;font-size:10px}
</style>
</head>
<body>
  <header>
    <div class="brand">
      <span class="brand-dot"></span>
      <span class="brand-name">Bright Path Web Growth</span>
    </div>
    <nav class="main-nav">
      <a class="is-current" href="#">Home</a><span class="nav-sep"></span>
      <a href="#">Services</a><span class="nav-sep"></span>
      <a href="#">About us</a><span class="nav-sep"></span>
      <a href="#">Blog</a><span class="nav-sep"></span>
      <a href="#">Contact</a>
    </nav>
    <div class="call-us">CALL US (02) 5550 1947</div>
  </header>

  <main>
    <div class="content-panel"></div>

    <div class="world-map" role="img" aria-label="Red world map"></div>

    <section class="services">
      <h2>Services</h2>
      <ul>
        <li>Consulting &amp; strategy planning</li>
        <li>Search engine optimisation</li>
        <li>Pay per click</li>
        <li>Re-marketing</li>
      </ul>
    </section>

    <h1 class="headline">
      <span>“We Grow Your Business Online.</span>
      <span>Clear Aim, Clear Plan, Clear Team,</span>
      <span>Bright Path Web Growth”</span>
    </h1>

    <div class="photo photo--team" role="img" aria-label="Business team holding up a rising bar chart"></div>
    <div class="photo photo--signing" role="img" aria-label="Hands signing a document"></div>
    <div class="photo photo--devices" role="img" aria-label="Tablet and devices on a desk"></div>

    <h3 class="testimonials-title">WHAT PEOPLE SAY:</h3>
    <blockquote class="testimonial t1">
      <p>aenean nomunny hendrerit mau phasellu porta, fusce suscipit varius mi sed, cum socrs natoque pernati-bus et magnis dis parturient montes, mascetur ridiculus mus, nulla dui</p>
      <p class="who">Lena Marsh</p>
      <p class="site">http://clientsite.org</p>
    </blockquote>
    <blockquote class="testimonial t2">
      <p>aenean nomunny hendrerit mau phasellu porta, fusce suscipit varius mi sed, cum socrs natoque pernati-bus et magnis dis parturient montes, mascetur ridiculus mus, nulla dui</p>
      <p class="who">Lena Marsh</p>
      <p class="site">http://clientsite.org</p>
    </blockquote>
    <blockquote class="testimonial t3">
      <p>aenean nomunny hendrerit mau phasellu porta, fusce suscipit varius mi sed, cum socrs natoque pernati-bus et magnis dis parturient montes, mascetur ridiculus mus, nulla dui</p>
      <p class="who">Lena Marsh</p>
      <p class="site">http://clientsite.org</p>
    </blockquote>
    <a class="see-all">see all the testimonials</a>

    <aside class="offer">
      <div class="offer-badge">Free</div>
      <span class="offer-line offer-line--sessions">strategy sessions</span>
      <span class="offer-line offer-line--here">HERE</span>
      <span class="offer-line offer-line--leads"><span>“</span>Double your leads<span>”</span></span>
    </aside>

    <form class="lead-form">
      <label style="top:31px">name</label><span class="field" style="top:46px"></span>
      <label style="top:65px">email</label><span class="field" style="top:80px"></span>
      <label style="top:100px">phone</label><span class="field" style="top:117px"></span>
      <label style="top:140px">website</label><span class="field" style="top:156px"></span>
      <button type="button">enquire now</button>
    </form>
  </main>

  <footer class="site-footer">All rights reserved Bright Path Web Growth, copyright c 2012</footer>
</body>
</html>
```